Tarnby Group letterhead

Hi,

I need a letterhead template created for our business. This should be done in word format and A4 size. The images need to not move in the template ie when I am adding writing in etc. and should flow on when I get to a second page.

I have attached our logo templates below.

Other details to include on the letterhead somewhere are:

0438 915 267
Max@Tarnbyelectrical.example.au
PO Box 817 Marrowvale NSW 2190
ABN: 57 318 962 407

Thanks!

```html
<!DOCTYPE html>
<html lang="en">
<head>
<meta charset="utf-8">
<title>Tarnby Group Letterhead</title>
<link href="https://fonts.googleapis.com/css2?family=Poppins:wght@400&display=swap" rel="stylesheet">
<style>
  :root {
    --orange: #f55105;
    --grey: #737373;
    --charcoal: #333333;
    --ink: #111111;
    --paper: #ffffff;
  }
  html, body {
    margin: 0;
    padding: 0;
    overflow: hidden;
    background: var(--paper);
  }
  .letterhead {
    position: relative;
    width: 1200px;
    height: 381px;
    overflow: hidden;
    background: var(--paper);
    font-family: "Poppins", sans-serif;
  }
  .contact-list {
    position: absolute;
    left: 120px;
    top: 148px;
    margin: 0;
    padding: 0;
    list-style: none;
  }
  .contact-item {
    display: flex;
    align-items: center;
    height: 30.5px;
    margin-bottom: 14px;
  }
  .contact-icon {
    width: 30.5px;
    height: 30.5px;
    flex: none;
    display: flex;
    align-items: center;
    justify-content: center;
  }
  .contact-icon.is-orange { background: var(--orange); }
  .contact-icon.is-grey { background: var(--grey); }
  .contact-icon svg { width: 20px; height: 20px; }
  .contact-text {
    margin-left: 15px;
    font-size: 20.5px;
    line-height: 1;
    color: var(--ink);
    letter-spacing: 0.2px;
    white-space: nowrap;
  }
  .corner-shapes {
    position: absolute;
    right: 0;
    top: 0;
    width: 1200px;
    height: 381px;
    pointer-events: none;
  }
</style>
</head>
<body>
<div class="letterhead">
  <ul class="contact-list">
    <li class="contact-item">
      <span class="contact-icon is-orange">
        <svg viewBox="0 0 24 24" aria-hidden="true">
          <path d="M6.6 3.2c.6-.4 1.4-.2 1.7.4l1.6 3c.3.6.1 1.2-.4 1.6l-1.3.9c.9 2.6 2.7 4.9 5 6.4l1.1-1.1c.5-.5 1.2-.5 1.7-.2l2.8 1.9c.6.4.7 1.2.3 1.7l-1.3 1.6c-.6.8-1.7 1.1-2.6.7C10 18 5.8 13.3 4.4 7.5c-.2-.9.1-1.9.9-2.5z" fill="#ffffff"/>
        </svg>
      </span>
      <span class="contact-text">0438 915 267</span>
    </li>
    <li class="contact-item">
      <span class="contact-icon is-grey">
        <svg viewBox="0 0 24 24" aria-hidden="true">
          <rect x="3" y="5.5" width="18" height="13" rx="1" fill="#ffffff"/>
          <path d="M3.5 6.5 12 12.5l8.5-6" fill="none" stroke="#737373" stroke-width="1.4"/>
        </svg>
      </span>
      <span class="contact-text">Max@Tarnbyelectrical.example.au</span>
    </li>
    <li class="contact-item">
      <span class="contact-icon is-orange">
        <svg viewBox="0 0 24 24" aria-hidden="true">
          <path d="M12 2.5c-3.9 0-7 3-7 6.8 0 4.6 7 12.2 7 12.2s7-7.6 7-12.2c0-3.8-3.1-6.8-7-6.8z" fill="#ffffff"/>
          <circle cx="12" cy="9.2" r="2.3" fill="#f55105"/>
        </svg>
      </span>
      <span class="contact-text">PO Box 817 Marrowvale NSW 2190</span>
    </li>
    <li class="contact-item">
      <span class="contact-icon is-grey">
        <svg viewBox="0 0 24 24" aria-hidden="true">
          <rect x="2.5" y="4" width="19" height="16" rx="2" fill="#ffffff" stroke="#111111" stroke-width="1.2"/>
          <path d="M2.5 7.5h19M2.5 10.5l8 2.5 11-3" fill="none" stroke="#111111" stroke-width="1.2"/>
        </svg>
      </span>
      <span class="contact-text">ABN: 57 318 962 407</span>
    </li>
  </ul>

  <svg class="corner-shapes" viewBox="0 0 1200 381" aria-hidden="true">
    <polygon points="960,143.5 722,381 1200,381 1200,381" fill="var(--charcoal)"/>
    <polygon points="1200,11.5 1017,191 1200,373" fill="var(--orange)"/>
    <polygon points="1011,11.5 1100,99.5 1012,188 923,99.5" fill="var(--grey)"/>
  </svg>
</div>
</body>
</html>
```